Etiketten für neue Biermarke
Zielgruppe
Es soll eine neue Biermarke entwickelt werden. Die fünf grundlegenden Sorten sind: Pils, Radler, Helles, Hefeweizen, Alkoholfreies Hefeweizen. Für die neue Biermarke soll ein Markenname, ein Logo, ein Etikettendesign, ein Kistendesign und erste Werbeentwürfe gestaltet werden.
Das Bier soll durch Modernität, Massentauglichkeit und das gewisse Etwas überzeugen und sympathisch, qualitativ und „cool“ auf die Käufer wirken.
Die Zielgruppe der Biermarke sind eher junge Bierliebhaber. Das Bier soll im mittleren Preissegment verkauft werden.
Aufgabenstellung
Eurer Fantasie sind keine Grenzen gesetzt. Der Markenname kann beispielsweise ein Lebensgefühl oder eine Vision vermitteln, die unsere Biermarke widerspiegelt und positive Assoziationen bei den Käufern hervorruft. Das Design soll kreativ und modern sein und nicht klassisch wirken.
Unser Bier sollte weder in die Richtung Craft Bier noch in die Richtung klassisches Braubier gehen.

```html
<!DOCTYPE html>
<html lang="de">
<head>
<meta charset="utf-8">
<title>Mr. Metro – Hefeweizen Etikett</title>
<link href="https://fonts.googleapis.com/css2?family=Josefin+Sans:wght@400;600&family=Russo+One&display=swap" rel="stylesheet">
<style>
  :root {
    --page: #ffffff;
    --band-green: #a8b038;
    --label-deep: #163e52;
    --label-teal: #1d5a62;
    --ray-dark: #0f2c3c;
    --skyline-teal: #2a9d8a;
    --figure-blue: #6cc7e6;
    --type-white: #ffffff;
    --type-soft: #eef3f0;
  }
  * { margin: 0; padding: 0; box-sizing: border-box; }
  html, body {
    width: 1200px;
    height: 1095px;
    overflow: hidden;
    background: var(--page);
  }
  .canvas {
    position: relative;
    width: 1200px;
    height: 1095px;
  }
  .label {
    position: absolute;
    left: 288px;
    top: 57px;
    width: 624px;
    height: 980px;
    overflow: hidden;
    background:
      radial-gradient(ellipse at 50% 45%, var(--label-teal) 0%, var(--label-deep) 55%, var(--ray-dark) 100%);
  }
  .variety-band {
    position: absolute;
    left: 0; top: 0;
    width: 100%;
    height: 105px;
    background: var(--band-green);
    display: flex;
    align-items: center;
    justify-content: center;
  }
  .variety-name {
    font-family: "Josefin Sans", sans-serif;
    font-weight: 400;
    font-size: 36px;
    letter-spacing: 0.42em;
    padding-left: 0.42em;
    color: var(--type-soft);
    margin-top: 14px;
  }
  .hero-art {
    position: absolute;
    left: 70px;
    top: 240px;
    width: 518px;
    height: 395px;
  }
  .brand-name {
    position: absolute;
    left: 0;
    width: 100%;
    text-align: center;
    font-family: "Russo One", sans-serif;
    color: var(--type-white);
    line-height: 1;
  }
  .brand-name--top {
    top: 628px;
    font-size: 136px;
    letter-spacing: -0.02em;
  }
  .brand-name--bottom {
    top: 745px;
    font-size: 150px;
    letter-spacing: -0.01em;
  }
  .label-facts {
    position: absolute;
    left: 37px;
    right: 37px;
    top: 916px;
    display: flex;
    justify-content: space-between;
    font-family: "Josefin Sans", sans-serif;
    font-size: 29px;
    letter-spacing: 0.06em;
    color: var(--type-soft);
  }
  .label-facts span + span { word-spacing: 0.3em; }
</style>
</head>
<body>
  <main class="canvas">
    <section class="label">
      <header class="variety-band">
        <span class="variety-name">HEFEWEIZEN</span>
      </header>

      <svg class="hero-art" viewBox="0 0 518 395" role="img" aria-label="Illustration: Saxofonspieler als hellblaue Silhouette vor türkiser Stadtsilhouette mit Strahlenkranz">
        <defs>
          <linearGradient id="hero-fill" x1="0" y1="0" x2="0" y2="1">
            <stop offset="0" stop-color="#1d5a62" stop-opacity="0"/>
            <stop offset="0.45" stop-color="#2a8a82" stop-opacity="0.55"/>
            <stop offset="1" stop-color="#2a9d8a" stop-opacity="0.75"/>
          </linearGradient>
        </defs>
        <rect width="518" height="395" fill="url(#hero-fill)"/>
      </svg>

      <div class="brand-name brand-name--top">MR.</div>
      <div class="brand-name brand-name--bottom">METRO</div>

      <footer class="label-facts">
        <span>5,2% VOL</span>
        <span>0,33 L</span>
      </footer>
    </section>
  </main>
</body>
</html>
```